Personal training poster - 1200X900mm

Poster to promote my new personal training service at my gym. The poster will be printed and put into an aframe to be seen by people walking past my gym. It needs to be simple and eye catching with the text i have put in the must haves. The text and image should be the prominent parts of the design.

Target Market(s)

30-50 year old females

Industry/Entity Type

Fitness

Font styles to use
Sans Serif

Requirements
Must have
• my logo
• exercise graphic
• Must include the following text:
• Are you looking for a personal trainer? Our expert trainers can help you achieve you take your health and fitness back!
• Contact details:
• 1300452968
• info@brightmovegym.com.au
• Located under the Harbourview Club

```html
<!DOCTYPE html>
<html lang="en">
<head>
<meta charset="utf-8">
<title>Personal Training Poster – Brightmove Gym</title>
<link rel="stylesheet" href="https://fonts.googleapis.com/css2?family=Barlow+Condensed:ital,wght@0,400;0,600;1,400;1,700;1,800&display=swap">
<style>
  :root {
    --page-bg: #eeeeee;
    --sky-light: #2ccbf0;
    --sky-mid: #1eaed8;
    --sky-deep: #147fa6;
    --violet: #3f3e8f;
    --sun: #f7cf57;
    --white: #ffffff;
    --logo-blue: #2a63b8;
  }
  * { margin: 0; padding: 0; box-sizing: border-box; }
  html, body {
    width: 1200px; height: 1064px; overflow: hidden;
    background: var(--page-bg);
  }
  .poster {
    position: absolute; left: 225px; top: 32px;
    width: 750px; height: 1000px; overflow: hidden;
    background: linear-gradient(100deg, var(--sky-light) 0%, var(--sky-mid) 55%, var(--sky-deep) 100%);
    font-family: "Barlow Condensed", "Arial Narrow", sans-serif;
    box-shadow: 0 6px 24px rgba(0,0,0,0.18);
  }
  .athlete-echo {
    position: absolute; left: 70px; top: 0; width: 640px; height: 960px;
    background: radial-gradient(ellipse 45% 55% at 55% 45%, rgba(63,62,143,0.75), rgba(63,62,143,0.25) 65%, rgba(63,62,143,0) 100%);
  }
  .athlete {
    position: absolute; left: 195px; top: 105px; width: 350px; height: 840px;
    background: radial-gradient(ellipse 50% 50% at 50% 45%, #d9a58c 0%, #b98370 40%, rgba(60,60,70,0.55) 75%, rgba(60,60,70,0) 100%);
  }
  .frames { position: absolute; inset: 0; }
  .brand-tab {
    position: absolute; left: 0; top: 0; width: 225px; height: 181px;
    background: var(--white);
    clip-path: polygon(0 0, 100% 0, 100% 75%, 0 100%);
    display: flex; align-items: center; justify-content: center; gap: 10px;
    padding-bottom: 30px;
  }
  .brand-mark { width: 26px; height: 26px; background: var(--logo-blue); }
  .brand-name {
    font-weight: 600; font-size: 30px; color: var(--logo-blue);
    text-transform: uppercase; letter-spacing: 1px; line-height: 1;
  }
  .headline {
    position: absolute; left: 382px; top: 393px; width: 760px;
    transform: translate(-50%, -50%) rotate(-19deg);
    text-align: center; color: var(--sun);
  }
  .headline-kicker {
    font-style: italic; font-weight: 700; font-size: 34px;
    text-transform: uppercase; letter-spacing: 1px; line-height: 1;
  }
  .headline-main {
    font-style: italic; font-weight: 800; font-size: 88px;
    text-transform: uppercase; line-height: 0.95; letter-spacing: 1px;
  }
  .headline-sub {
    font-style: italic; font-weight: 400; font-size: 22px; line-height: 1.3;
    margin-top: 6px;
  }
  .contact-list { position: absolute; left: 52px; top: 800px; list-style: none; }
  .contact-item {
    display: flex; align-items: center; gap: 18px;
    height: 66px; color: var(--white); font-size: 20px; letter-spacing: 0.5px;
  }
  .contact-icon { width: 26px; height: 26px; flex: none; }
</style>
</head>
<body>
  <main class="poster">
    <div class="athlete-echo" role="img" aria-label="Large faded violet-toned image of the athlete in a running pose"></div>

    <svg class="frames" width="750" height="1000" viewBox="0 0 750 1000" aria-hidden="true">
      <g fill="none" stroke="#f7cf57" stroke-width="3">
        <polyline points="218,44 695,44 695,175 62,395"/>
        <polyline points="60,640 60,759 690,759"/>
        <line x1="60" y1="640" x2="60" y2="530"/>
      </g>
      <g fill="#f7cf57">
        <rect x="498" y="197" width="18" height="18"/>
        <rect x="591" y="248" width="12" height="12"/>
        <rect x="209" y="234" width="28" height="28" opacity="0.55"/>
        <rect x="230" y="547" width="50" height="50" opacity="0.7"/>
        <rect x="260" y="572" width="65" height="95" opacity="0.45"/>
        <rect x="528" y="455" width="52" height="52" opacity="0.45"/>
      </g>
    </svg>

    <div class="athlete" role="img" aria-label="Woman in sportswear and trainers jumping with one knee raised"></div>

    <header class="brand-tab">
      <span class="brand-mark"></span>
      <span class="brand-name">Brightmove Gym</span>
    </header>

    <section class="headline">
      <p class="headline-kicker">Are you looking for a</p>
      <h1 class="headline-main">Personal Trainer?</h1>
      <p class="headline-sub">Our experts can help you achieve you take your health and fitness back!</p>
    </section>

    <ul class="contact-list">
      <li class="contact-item">
        <svg class="contact-icon" viewBox="0 0 24 24" fill="none" stroke="#fff" stroke-width="1.6" stroke-linejoin="round"><path d="M5 3h4l2 5-2.5 1.5a11 11 0 0 0 6 6L16 13l5 2v4a2 2 0 0 1-2 2A16 16 0 0 1 3 5a2 2 0 0 1 2-2z"/><path d="M15 3a6 6 0 0 1 6 6M15 6.5a2.5 2.5 0 0 1 2.5 2.5"/></svg>
        <span>1300452968</span>
      </li>
      <li class="contact-item">
        <svg class="contact-icon" viewBox="0 0 24 24" fill="none" stroke="#fff" stroke-width="1.6"><rect x="3" y="5" width="18" height="14" rx="1"/><path d="M3 6l9 7 9-7"/></svg>
        <span>info@brightmovegym.com.au</span>
      </li>
      <li class="contact-item">
        <svg class="contact-icon" viewBox="0 0 24 24" fill="none" stroke="#fff" stroke-width="1.6"><path d="M12 22s7-7 7-12a7 7 0 0 0-14 0c0 5 7 12 7 12z"/><circle cx="12" cy="10" r="2.5"/></svg>
        <span>Located under the Harbourview Club</span>
      </li>
    </ul>
  </main>
</body>
</html>
```